Design a cool print brochure for an NGO / Give your work a global impact!!

Hi,
I provide a full design brief (below, please scroll) and a mood board (attached) to help you visualize inside my head.. ;-)
I am also available to help and have worked many years in advertising; we will understand each other.
Objective:
To design an A4 folded in two presentation brochure for a non-profit consulting agency called Vantriq.
Vantriq works in sustainability and international development = working with NGO’s, governments and private sector on global issues such as global warming, education for all etc.
Strategy:
This document is a first step in developing a communication strategy. It will be distributed during a major international event called the Meridale Outreach Forum.
Objective:
The double objective of the brochure is:
a) to inform the recipient of what Vantriq is, in the shortest time possible.
b) to showcase relevant projects to demonstrate Vantriq experience and expertise.
Target:
Main target:
Existing Vantriq contacts, such as members of development organizations, NGOs, private sector foundations (CSR), regional networks and other development actors.
NB: the main target already has a certain awareness of Vantriq: we will try to minimize text to maximize visual impact and readability.
Secondary target:
Vantriq will also distribute the brochure to new prospects of interest during the Meridale Forum.
Timing:
We will need to finalize the design and have the files by June 1st to allow time for print before the event.
Content:
The document should be concise, highly readable (no clutter) and include:
1. text (that we will provide)
and
2. visual elements such as images, shapes and info-graphics (that is you).
NB: Vantriq does not have its own image bank; photos will be provided by you.
Format:
A4 folded in half - 4pp A5 - PORTRAIT FORMAT) with an impactful visual in the front, logo, title and headline (please see examples in the mood board attached).
Design elements:
Vantriq does not have yet a visual identity (please see: http://vantriq.org) so there is room for creativity and no graphic chart to follow.
The sector of consulting in international development is rather conservative but our intention is to be disruptive and create a “Wow” effect. We count on you for that!
Therefore, the design should be “structured”, “organized”, “uncluttered” but also “modern”, “impactful”, “highly visual” (think infographic or mind map to describe our services and projects).
Please, take the time to see the attached presentation: I give you guidelines and examples of what we want and what we like.
We are looking forward to seeing your work and I am available for comments, questions and support.
Thank you.
RK
Target Market(s)
The full brief is in the project description: please, scroll through it.
The target market is : our existing clients base, working in sustainable development (read: NGO and Allied Assembly people)
Industry/Entity Type
Ngo
Font styles to use
Requirements
Must have
- - Design and color elements: please, no black and white. Our company website is in black and white and without graphics; we want the brochure to break away from that and start creating our brand identity; so please, show us colors and desing elements (shapes, backgrounds, etc).
- You have a chance to showcase your talent in terms of visual identity: what lines, forms, layout and colors can you come up with and apply throughout the brochure and serve as the visual identity of Vantriq?
- The structure of the document should be:
- - Front cover: design elements + impacful photo (see mood board example attached) +our logo + this headline: "Collective action for sustainable development and impact"
- - Inside front: a graphic representation of "Our Services": such as core activity in the center circle and satellite circles for the services we offer.
- - Inside back:
- 1. Icons and text boxes for "Our projects"
- 2. A world map of the countries where we have worked. Full list of countries is here:
- http://vantriq.org/experience-1
- - Back cover: our contact + logos of partners.
- Our partners are listed here:
- Please use their original logos (ie, in color).
- The design we will select will serve as a basis for a graphic chart...so more work to come...word to the wise ;)
- Please check out our website vantriq.org to see what we do etc.
Nice to have
- Icons to reflect our services: what icons can you come up with to describe "training services", "building networks" or "program management"?
- I give examples in the mood board.
Should not have
- We are open to creativity and want to generate a "Wow" effect.
- Just note that the sector is rather conservative so flashy colors and cartoon like characters should be avoided. Think "earth, global change, Allied Assembly, climate" without going too green (it's overdone). ;-)
- Make us stand out in the NGO world
- Now you.

```html
<!DOCTYPE html>
<html lang="en">
<head>
<meta charset="utf-8">
<title>Vantriq Brochure</title>
<link href="https://fonts.googleapis.com/css2?family=Montserrat:wght@400;500;600;700&family=Open+Sans:wght@400;600&display=swap" rel="stylesheet">
<style>
  :root{
    --bg:#e8e8e8;
    --paper:#ffffff;
    --gold:#d6ab45;
    --gold-light:#efd27e;
    --gold-deep:#b8892c;
    --ink:#2a2a2a;
    --grey:#666666;
    --grey-soft:#bdbdbd;
    --shade:#f1f1f1;
  }
  *{box-sizing:border-box;margin:0;padding:0}
  html,body{width:739px;height:1200px;overflow:hidden;background:var(--bg)}
  body{position:relative;font-family:"Open Sans",Arial,sans-serif;color:var(--ink)}
  .piece-label{position:absolute;font-family:"Montserrat",Arial,sans-serif;font-size:16px;font-weight:500;color:var(--ink)}
  .page{position:absolute;background:var(--paper);box-shadow:0 6px 18px rgba(0,0,0,.18);overflow:hidden}
  .page svg.art{position:absolute;inset:0;width:100%;height:100%}
  .cover{width:330px;height:467px;top:56px}
  .cover--back{left:24px}
  .cover--front{left:385px}
  .spread{left:24px;top:640px;width:690px;height:488px}

  .brand{position:absolute;display:flex;align-items:center;gap:8px}
  .brand__name{font-family:"Montserrat",Arial,sans-serif;font-weight:600;color:var(--grey);letter-spacing:.5px}
  .brand__rule{width:1.5px;align-self:stretch;background:var(--grey)}
  .brand__tagline{font-family:"Montserrat",Arial,sans-serif;font-size:8px;line-height:1.15;color:var(--grey)}
  .cover--front .brand{left:26px;top:34px}
  .cover--front .brand__name{font-size:38px}
  .web{position:absolute;font-family:"Montserrat",Arial,sans-serif;font-size:9px;letter-spacing:2px;color:var(--ink);font-weight:500}
  .cover--front .web{right:30px;bottom:26px}

  .partners{position:absolute;left:0;top:22px;width:100%;text-align:center}
  .section-title{font-family:"Montserrat",Arial,sans-serif;font-weight:700;font-size:12px;letter-spacing:.5px;color:var(--ink)}
  .partners__grid{display:flex;flex-wrap:wrap;justify-content:center;gap:10px 14px;margin:12px auto 0;width:280px}
  .partner-badge{width:46px;height:22px;border-radius:3px;background:var(--shade);border:1px solid #dedede}
  .partner-badge--round{width:24px;border-radius:50%}
  .contact-bubble{position:absolute;left:110px;top:188px;width:160px;height:160px;border-radius:50%;color:#fff;text-align:center;padding:34px 18px 0}
  .contact-bubble h3{font-family:"Montserrat",Arial,sans-serif;font-size:11px;font-weight:600;margin-bottom:8px}
  .contact-bubble p{font-size:7.2px;line-height:1.4;margin-bottom:6px}
  .cover--back .brand{left:28px;top:372px}
  .cover--back .brand__name{font-size:22px;color:#fff}
  .cover--back .brand__rule{background:#fff}
  .cover--back .brand__tagline{color:#fff;font-size:5.5px}
  .contact-line{position:absolute;display:flex;align-items:center;gap:5px;font-size:8px;color:var(--ink);font-weight:600}
  .contact-line svg{width:10px;height:10px}
  .contact-line--phone{left:28px;top:418px}
  .contact-line--mail{left:190px;top:384px}
  .cover--back .web{left:110px;top:438px;font-size:8px}

  .services-title{position:absolute;left:120px;top:34px}
  .service-label{position:absolute;font-family:"Montserrat",Arial,sans-serif;font-size:6.5px;line-height:1.25;color:var(--ink);width:90px}
  .projects-title{position:absolute;left:430px;top:34px}
  .project-list{position:absolute;left:392px;top:62px;width:270px;list-style:none}
  .project{display:flex;gap:8px;align-items:center;margin-bottom:9px}
  .project__icon{flex:0 0 18px;height:18px;border-radius:50%;border:1.5px solid var(--gold);display:flex;align-items:center;justify-content:center}
  .project__icon svg{width:9px;height:9px}
  .project p{font-size:6.2px;line-height:1.35;color:var(--ink)}
  .fold{position:absolute;left:345px;top:0;width:1px;height:100%;background:linear-gradient(#e2e2e2,#cfcfcf,#e2e2e2)}
</style>
</head>
<body>

<span class="piece-label" style="left:560px;top:24px">Front</span>
<span class="piece-label" style="left:150px;top:24px">Back</span>
<span class="piece-label" style="left:320px;top:1150px">Inner Side</span>

<!-- Back cover -->
<section class="page cover cover--back">
  <svg class="art" viewBox="0 0 330 467" preserveAspectRatio="none">
    <defs>
      <linearGradient id="backPhoto" x1="0" y1="0" x2="1" y2="1">
        <stop offset="0" stop-color="#3c3a38"/><stop offset=".5" stop-color="#7b746b"/><stop offset="1" stop-color="#c9b9a3"/>
      </linearGradient>
      <linearGradient id="goldBand" x1="0" y1="0" x2="1" y2="1">
        <stop offset="0" stop-color="#e7c56b"/><stop offset=".6" stop-color="#d6ab45"/><stop offset="1" stop-color="#b8892c"/>
      </linearGradient>
    </defs>
    <path d="M0,170 C120,150 250,120 330,95 L330,108 C250,133 120,164 0,184 Z" fill="var(--gold)"/>
    <path role="img" aria-label="Photo of business colleagues shaking hands in a bright office" d="M0,184 C120,164 250,133 330,108 L330,330 C220,360 100,390 0,404 Z" fill="url(#backPhoto)"/>
    <path d="M0,404 C100,390 220,360 330,330 L330,467 L0,467 Z" fill="url(#goldBand)"/>
    <path d="M0,400 C100,386 220,356 330,326" stroke="#fff" stroke-width="2" fill="none"/>
  </svg>
  <div class="partners">
    <h2 class="section-title">OUR PARTNERS</h2>
    <div class="partners__grid">
      <span class="partner-badge partner-badge--round"></span>
      <span class="partner-badge"></span><span class="partner-badge"></span>
      <span class="partner-badge"></span><span class="partner-badge"></span>
      <span class="partner-badge"></span><span class="partner-badge"></span>
      <span class="partner-badge"></span><span class="partner-badge"></span>
      <span class="partner-badge"></span>
    </div>
  </div>
  <div class="contact-bubble" style="background:rgba(85,85,85,.86)">
    <h3>CONTACT US</h3>
    <p>We are based in different cities in Europe. You can contact any of us directly in About Us.</p>
    <p>Alternatively, for general inquiries, you can use the number and/or email below</p>
  </div>
  <div class="brand">
    <span class="brand__name">Vantriq</span><span class="brand__rule"></span>
    <span class="brand__tagline">Analysis<br>&amp; Advisory Services<br>for effective<br>collaborative action</span>
  </div>
  <div class="contact-line contact-line--mail">
    <svg viewBox="0 0 10 10"><circle cx="5" cy="5" r="5" fill="var(--ink)"/><rect x="2.4" y="3.3" width="5.2" height="3.6" fill="none" stroke="#fff" stroke-width=".7"/><path d="M2.4,3.3 L5,5.4 L7.6,3.3" fill="none" stroke="#fff" stroke-width=".7"/></svg>
    info@vantriq.org
  </div>
  <div class="contact-line contact-line--phone">
    <svg viewBox="0 0 10 10"><circle cx="5" cy="5" r="5" fill="var(--ink)"/><path d="M3.3,2.6 L4.3,2.6 L4.7,3.9 L4.1,4.4 C4.5,5.2 5,5.7 5.7,6 L6.2,5.4 L7.4,5.8 L7.4,6.8 C5.2,7 3.1,4.9 3.3,2.6 Z" fill="#fff"/></svg>
    +00 555 014 270
  </div>
  <span class="web">www.vantriq.org</span>
</section>

<!-- Front cover -->
<section class="page cover cover--front">
  <svg class="art" viewBox="0 0 330 467" preserveAspectRatio="none">
    <defs>
      <linearGradient id="frontPhoto" x1="0" y1="0" x2="1" y2="1">
        <stop offset="0" stop-color="#d9d2c6"/><stop offset=".45" stop-color="#8a6a4a"/><stop offset="1" stop-color="#2e2520"/>
      </linearGradient>
      <linearGradient id="goldFront" x1="0" y1="0" x2="1" y2="1">
        <stop offset="0" stop-color="#efd27e"/><stop offset=".55" stop-color="#d6ab45"/><stop offset="1" stop-color="#b8892c"/>
      </linearGradient>
    </defs>
    <path d="M0,168 C110,116 230,92 330,84 L330,96 C230,104 110,128 0,182 Z" fill="var(--gold)"/>
    <path role="img" aria-label="Photo of hands working on papers and a laptop at a desk with drinks" d="M0,182 C110,128 230,104 330,96 L330,350 C220,384 110,396 0,392 Z" fill="url(#frontPhoto)"/>
    <path d="M0,392 C110,396 220,384 330,350 L330,200 C300,300 220,380 0,392 Z" fill="#1f1f1f" opacity=".85"/>
    <path d="M0,392 C110,396 220,384 330,350 L330,467 L0,467 Z" fill="url(#goldFront)"/>
    <path d="M0,388 C110,392 220,380 330,346" stroke="#fff" stroke-width="2" fill="none"/>
    <path d="M0,428 C110,430 220,420 330,400 L330,467 L0,467 Z" fill="#fff" opacity=".12"/>
  </svg>
  <div class="brand">
    <span class="brand__name">Vantriq</span><span class="brand__rule"></span>
    <span class="brand__tagline">Analysis<br>&amp; Advisory Services<br>for effective<br>collaborative action</span>
  </div>
  <span class="web">www.vantriq.org</span>
</section>

<!-- Inner spread -->
<section class="page spread">
  <svg class="art" viewBox="0 0 690 488" preserveAspectRatio="none">
    <defs>
      <linearGradient id="servicePhoto" x1="0" y1="0" x2="1" y2="0">
        <stop offset="0" stop-color="#5a4a78"/><stop offset=".5" stop-color="#a99abf"/><stop offset="1" stop-color="#e7e1ee"/>
      </linearGradient>
      <linearGradient id="dealPhoto" x1="0" y1="0" x2="1" y2="1">
        <stop offset="0" stop-color="#dfe3e6"/><stop offset=".6" stop-color="#8b9096"/><stop offset="1" stop-color="#2b2f36"/>
      </linearGradient>
      <radialGradient id="thumb" cx=".4" cy=".35" r=".7">
        <stop offset="0" stop-color="#dcdcdc"/><stop offset="1" stop-color="#6e6e6e"/>
      </radialGradient>
    </defs>
    <!-- bottom bands -->
    <path d="M0,352 C120,392 240,398 345,372 L345,386 C240,412 120,406 0,366 Z" fill="var(--gold)"/>
    <path role="img" aria-label="Photo of a person typing on a laptop beside a coffee cup" d="M0,366 C120,406 240,412 345,386 L345,488 L0,488 Z" fill="url(#servicePhoto)"/>
    <path d="M345,372 C450,340 560,300 690,280 L690,292 C560,312 450,352 345,386 Z" fill="var(--gold)"/>
    <path role="img" aria-label="Photo of two business people shaking hands" d="M345,386 C450,352 560,312 690,292 L690,488 L345,488 Z" fill="url(#dealPhoto)"/>

    <!-- services mind map -->
    <g fill="none" stroke="var(--gold)" stroke-width="1.5">
      <path d="M70,200 A90,90 0 0 1 250,160"/>
      <path d="M70,200 A90,100 0 0 0 150,305"/>
      <path d="M150,305 A100,100 0 0 0 250,250"/>
      <path d="M250,160 L262,190 L250,250"/>
    </g>
    <g fill="var(--gold)">
      <circle cx="96" cy="206" r="3"/><circle cx="115" cy="263" r="3"/><circle cx="168" cy="300" r="3"/>
      <circle cx="218" cy="132" r="3"/><circle cx="244" cy="175" r="3"/><circle cx="240" cy="240" r="3"/>
    </g>
    <circle cx="160" cy="205" r="62" fill="#f4f4f4"/>
    <circle cx="160" cy="205" r="48" fill="#e9e9e9"/>
    <circle cx="160" cy="205" r="36" fill="#fff"/>
    <g transform="translate(160 205)" fill="none" stroke="#555" stroke-width="3">
      <circle r="10" stroke-dasharray="4 3"/>
      <circle r="4" stroke-width="2"/>
    </g>
    <g stroke="var(--gold)" stroke-width="2.5">
      <circle cx="72" cy="200" r="24" fill="url(#thumb)" role="img" aria-label="Photo of research documents"/>
      <circle cx="88" cy="285" r="24" fill="url(#thumb)" role="img" aria-label="Photo of a facilitated group meeting"/>
      <circle cx="150" cy="330" r="24" fill="url(#thumb)" role="img" aria-label="Photo of an empty meeting room"/>
      <circle cx="218" cy="104" r="22" fill="url(#thumb)" role="img" aria-label="Photo of a conference hall"/>
      <circle cx="268" cy="170" r="22" fill="url(#thumb)" role="img" aria-label="Photo of a training session"/>
      <circle cx="262" cy="250" r="22" fill="url(#thumb)" role="img" aria-label="Photo of a laptop with charts"/>
    </g>
  </svg>
  <span class="fold"></span>

  <h2 class="section-title services-title">OUR SERVICES</h2>
  <span class="service-label" style="left:16px;top:150px">Research and Analysis of Cooperation Schemes</span>
  <span class="service-label" style="left:16px;top:250px;width:60px">Facilitation of Processes of Change</span>
  <span class="service-label" style="left:180px;top:318px;width:100px">Methodologies for Organizational Change and Consensus Building</span>
  <span class="service-label" style="left:244px;top:70px">Coalition Building to Achieve Collective Goals</span>
  <span class="service-label" style="left:292px;top:146px;width:52px">Training to Improve Networked Action</span>
  <span class="service-label" style="left:288px;top:226px;width:56px">Evaluation of Multi-actor Projects and Programs</span>

  <h2 class="section-title projects-title">OUR PROJECTS</h2>
  <ul class="project-list">
    <li class="project"><span class="project__icon"><svg viewBox="0 0 10 10"><path d="M1.5,5.2 L4,7.5 L8.5,2.5" fill="none" stroke="var(--gold)" stroke-width="1.5"/></svg></span><p>Lorem Ipsum is simply dummy text of the printing and typesetting industry. Lorem Ipsum has been the industry's standard dummy text ever since the 1500s, when an unknown printer took a galley of type and scrambled it to make a type specimen.</p></li>
    <li class="project"><span class="project__icon"><svg viewBox="0 0 10 10"><path d="M1.5,5.2 L4,7.5 L8.5,2.5" fill="none" stroke="var(--gold)" stroke-width="1.5"/></svg></span><p>Lorem Ipsum is simply dummy text of the printing and typesetting industry. Lorem Ipsum has been the industry's standard dummy text ever since the 1500s, when an unknown printer took a galley of type and scrambled it to make a type specimen.</p></li>
    <li class="project"><span class="project__icon"><svg viewBox="0 0 10 10"><path d="M1.5,5.2 L4,7.5 L8.5,2.5" fill="none" stroke="var(--gold)" stroke-width="1.5"/></svg></span><p>Lorem Ipsum is simply dummy text of the printing and typesetting industry. Lorem Ipsum has been the industry's standard dummy text ever since the 1500s, when an unknown printer took a galley of type and scrambled it to make a type specimen.</p></li>
    <li class="project"><span class="project__icon"><svg viewBox="0 0 10 10"><path d="M1.5,5.2 L4,7.5 L8.5,2.5" fill="none" stroke="var(--gold)" stroke-width="1.5"/></svg></span><p>Lorem Ipsum is simply dummy text of the printing and typesetting industry. Lorem Ipsum has been the industry's standard dummy text ever since the 1500s, when an unknown printer took a galley of type and scrambled it to make a type specimen.</p></li>
    <li class="project"><span class="project__icon"><svg viewBox="0 0 10 10"><path d="M1.5,5.2 L4,7.5 L8.5,2.5" fill="none" stroke="var(--gold)" stroke-width="1.5"/></svg></span><p>Lorem Ipsum is simply dummy text of the printing and typesetting industry. Lorem Ipsum has been the industry's standard dummy text ever since the 1500s, when an unknown printer took a galley of type and scrambled it to make a type specimen.</p></li>
    <li class="project"><span class="project__icon"><svg viewBox="0 0 10 10"><path d="M1.5,5.2 L4,7.5 L8.5,2.5" fill="none" stroke="var(--gold)" stroke-width="1.5"/></svg></span><p>Lorem Ipsum is simply dummy text of the printing and typesetting industry. Lorem Ipsum has been the industry's standard dummy text ever since the 1500s, when an unknown printer took a galley of type and scrambled it to make a type specimen.</p></li>
  </ul>
</section>

</body>
</html>
```